Image / Drawing for the Home Page - Website

We need a photo / drawing for the home page of our website. We are in the process of finalizing our website, the current project includes a black photo too sad, too dark and not readable. Company name: ORME CONSEIL We are in La Rochelle (17000 - france) We are a financial consulting firm / Strategy and steering for SMEs Our slogan: Creator of Trust 100% digital - 100% human Present We have a main photo in black, it is too dark, we want to change it. (The current link http://webmirak.co.uk/orme-conseil/) We would like a white or light background, to make the page more attractive, easier to read, want to stay on the site. Our competitors: http://www.tirel-gestion.fr/ https://www.palmin.fr/ https://www.bivoucartelin.fr/

Target Market(s)

SME / TPE Hotel / Start-up / Web / digital

Industry/Entity Type

Hotel

Number of Pages Required

1 page

Font styles to use
Sans Serif

Colors

Designer to choose colors to be used in the design.

Requirements
Must have
• Image for home page
Nice to have
• We want an image for the home page of the site It must be: clear readable modern dynamic seriously chic preferably on a light background colors are black and orange

```html
<!DOCTYPE html>
<html lang="en">
<head>
<meta charset="utf-8">
<title>Orme Conseil – Home page hero concepts</title>
<link href="https://fonts.googleapis.com/css2?family=Open+Sans:wght@400;600;700;800&display=swap" rel="stylesheet">
<style>
:root{
  --orange:#f39200;
  --orange-dark:#d97e00;
  --ink:#2a2a2a;
  --ink-soft:#444;
  --grey:#8a8a8a;
  --page:#eef0f2;
  --white:#ffffff;
}
*{box-sizing:border-box;margin:0;padding:0}
html,body{width:1200px;height:2888px;overflow:hidden}
body{background:var(--page);font-family:"Open Sans",Arial,sans-serif;color:var(--ink);position:relative}

.concept{position:absolute;left:24px;width:1152px;height:640px;background:var(--white);overflow:hidden;box-shadow:0 2px 10px rgba(0,0,0,.15)}
.concept--one{top:20px}
.concept--two{top:760px}
.concept--three{top:1500px}
.concept--four{top:2240px}

/* top contact bar */
.topbar{height:26px;display:flex;justify-content:flex-end;align-items:center;gap:18px;padding:0 40px;font-size:11px;background:var(--ink);color:var(--white)}
.topbar--light{background:var(--white);color:var(--ink-soft)}
.topbar--orange{background:var(--orange);color:var(--ink)}
.topbar .socials{display:flex;gap:6px}
.topbar .socials span{width:11px;height:11px;border-radius:50%;background:currentColor;opacity:.8}
.contact-item{display:flex;align-items:center;gap:5px}

/* header */
.header{display:flex;align-items:center;justify-content:space-between;padding:0 40px;background:var(--white)}
.brand{display:flex;align-items:center;gap:12px}
.brand-mark{width:58px;height:58px;border-radius:50%;background:var(--ink)}
.brand-name{font-size:34px;font-weight:700;color:var(--ink);letter-spacing:.5px;line-height:1}
.brand-tagline{font-size:13px;color:var(--ink-soft);margin-top:4px}
.btn-quote{background:var(--ink);color:var(--white);font-size:13px;font-weight:700;padding:11px 30px;border-radius:4px}

/* navigation */
.nav{display:flex;background:var(--orange);color:var(--white);font-size:13px}
.nav-item{display:flex;flex-direction:column;align-items:center;justify-content:center;gap:4px;padding:0 22px}
.nav-item.is-active{background:var(--ink)}
.nav-icon{width:14px;height:14px}

/* hero */
.hero{position:relative}
.hero-photo{position:absolute;inset:0}
.hero-copy{position:absolute;left:0;right:0;text-align:center}
.hero-title{font-size:40px;font-weight:800;letter-spacing:.5px}
.hero-sub{font-size:14px;font-weight:600;margin-top:12px}
.btn-start{display:inline-block;margin-top:22px;background:var(--ink);color:var(--white);font-size:14px;font-weight:700;padding:13px 40px;border-radius:5px}
.title-light{color:var(--white);text-shadow:0 2px 6px rgba(0,0,0,.45)}
.title-orange{color:var(--orange);text-shadow:0 1px 2px rgba(0,0,0,.35)}
.sub-light{color:var(--white);text-shadow:0 1px 4px rgba(0,0,0,.5)}
.sub-dark{color:var(--ink)}
</style>
</head>
<body>

<!-- Concept 1 -->
<section class="concept concept--one">
  <div class="topbar">
    <span class="contact-item">✉ contact@orme-conseil.com</span>
    <span class="contact-item">☏ 05 46 12 34 56</span>
    <span class="socials"><span></span><span></span><span></span><span></span></span>
  </div>
  <header class="header" style="height:92px">
    <div class="brand"><span class="brand-mark"></span><div><div class="brand-name">ORME CONSEIL</div><div class="brand-tagline">Créateur de Confiance</div></div></div>
    <span class="btn-quote">GET A QUOTE</span>
  </header>
  <nav class="nav" style="height:42px;padding-left:40px">
    <span class="nav-item is-active"><svg class="nav-icon" viewBox="0 0 14 14"><path d="M1 7 7 1l6 6h-2v6H3V7z" fill="#fff"/></svg></span>
    <span class="nav-item">Gérer mon entreprise</span>
    <span class="nav-item">Avis d'Experts ▾</span>
    <span class="nav-item">Gérer mon personnel</span>
    <span class="nav-item">Mon statut dirigeant</span>
    <span class="nav-item">Mes finances</span>
    <span class="nav-item">Statut</span>
    <span class="nav-item">Contact</span>
  </nav>
  <div class="hero" style="height:480px">
    <div class="hero-photo" role="img" aria-label="Photo of a smiling business team in a bright office" style="background:linear-gradient(100deg,#6b6a6e 0%,#b9b6b4 30%,#e6e4e1 50%,#a7a4a6 72%,#3c4256 100%)"></div>
    <div class="hero-copy" style="top:188px">
      <div class="hero-title title-light">CREATOR OF TRUST 100% DIGITAL - 100% HUMAN</div>
      <div class="hero-sub sub-light">ORME CONSEIL is the result of a STRONG TECHNICAL AND MANAGERIAL EXPERIENCE</div>
    </div>
  </div>
</section>

<!-- Concept 2 -->
<section class="concept concept--two">
  <div class="topbar topbar--light">
    <span class="contact-item">✉ contact@orme-conseil.com</span>
    <span class="contact-item">☏ 05 46 12 34 56</span>
    <span class="socials"><span></span><span></span><span></span><span></span></span>
  </div>
  <header class="header" style="height:104px;position:relative;padding-right:0">
    <div class="brand"><span class="brand-mark"></span><div><div class="brand-name">ORME CONSEIL</div><div class="brand-tagline">Créateur de Confiance</div></div></div>
    <svg style="position:absolute;right:0;top:0" width="760" height="104" viewBox="0 0 760 104"><polygon points="60,0 760,0 760,104 0,104" fill="#f39200"/></svg>
    <nav class="nav" style="position:relative;height:104px;background:none;font-size:11px;padding-right:20px">
      <span class="nav-item is-active" style="padding:0 14px"><svg class="nav-icon" viewBox="0 0 14 14"><path d="M1 7 7 1l6 6h-2v6H3V7z" fill="#fff"/></svg>Home</span>
      <span class="nav-item" style="padding:0 9px"><svg class="nav-icon" viewBox="0 0 14 14"><rect x="2" y="4" width="10" height="8" fill="#fff"/></svg>Gérer mon entreprise</span>
      <span class="nav-item" style="padding:0 9px"><svg class="nav-icon" viewBox="0 0 14 14"><circle cx="7" cy="7" r="5" fill="#fff"/></svg>Avis d'Experts</span>
      <span class="nav-item" style="padding:0 9px"><svg class="nav-icon" viewBox="0 0 14 14"><circle cx="7" cy="5" r="3" fill="#fff"/><rect x="3" y="9" width="8" height="4" fill="#fff"/></svg>Gérer mon personnel</span>
      <span class="nav-item" style="padding:0 9px"><svg class="nav-icon" viewBox="0 0 14 14"><circle cx="7" cy="5" r="3" fill="#fff"/><rect x="3" y="9" width="8" height="4" fill="#fff"/></svg>Mon statut dirigeant</span>
      <span class="nav-item" style="padding:0 9px"><svg class="nav-icon" viewBox="0 0 14 14"><rect x="2" y="7" width="3" height="6" fill="#fff"/><rect x="6" y="4" width="3" height="9" fill="#fff"/><rect x="10" y="1" width="3" height="12" fill="#fff"/></svg>Mes finances</span>
      <span class="nav-item" style="padding:0 9px"><svg class="nav-icon" viewBox="0 0 14 14"><rect x="3" y="1" width="8" height="12" fill="#fff"/></svg>Statut</span>
      <span class="nav-item" style="padding:0 9px"><svg class="nav-icon" viewBox="0 0 14 14"><path d="M3 1h3l1 4-2 1c1 2 2 3 4 4l1-2 4 1v3c-6 0-11-5-11-11z" fill="#fff"/></svg>Contact</span>
    </nav>
  </header>
  <div class="hero" style="height:510px">
    <div class="hero-photo" role="img" aria-label="Photo of a consultant with glasses working at a desk" style="background:linear-gradient(100deg,#c9cbcf 0%,#e9eaec 35%,#bfbfc1 55%,#f2f2f3 80%,#dcdde0 100%)"></div>
    <div class="hero-copy" style="top:195px">
      <div class="hero-title title-light">CREATOR OF TRUST 100% DIGITAL - 100% HUMAN</div>
      <div class="hero-sub sub-light">ORME CONSEIL is the result of a STRONG TECHNICAL AND MANAGERIAL EXPERIENCE</div>
      <span class="btn-start">GET STARTED</span>
    </div>
  </div>
</section>

<!-- Concept 3 -->
<section class="concept concept--three">
  <div class="topbar">
    <span class="contact-item">✉ contact@orme-conseil.com</span>
    <span class="contact-item">☏ 05 46 12 34 56</span>
    <span class="socials"><span></span><span></span><span></span><span></span></span>
  </div>
  <header class="header" style="height:84px">
    <div class="brand"><span class="brand-mark"></span><div><div class="brand-name">ORME CONSEIL</div><div class="brand-tagline">Créateur de Confiance</div></div></div>
    <span class="btn-quote">GET A QUOTE</span>
  </header>
  <nav class="nav" style="height:52px;padding-left:40px;font-size:12px">
    <span class="nav-item is-active"><svg class="nav-icon" viewBox="0 0 14 14"><path d="M1 7 7 1l6 6h-2v6H3V7z" fill="#fff"/></svg>Home</span>
    <span class="nav-item"><svg class="nav-icon" viewBox="0 0 14 14"><rect x="2" y="4" width="10" height="8" fill="#fff"/></svg>Gérer mon entreprise</span>
    <span class="nav-item"><svg class="nav-icon" viewBox="0 0 14 14"><circle cx="7" cy="7" r="5" fill="#fff"/></svg>Avis d'Experts ▾</span>
    <span class="nav-item"><svg class="nav-icon" viewBox="0 0 14 14"><circle cx="7" cy="5" r="3" fill="#fff"/><rect x="3" y="9" width="8" height="4" fill="#fff"/></svg>Gérer mon personnel</span>
    <span class="nav-item"><svg class="nav-icon" viewBox="0 0 14 14"><circle cx="7" cy="5" r="3" fill="#fff"/><rect x="3" y="9" width="8" height="4" fill="#fff"/></svg>Mon statut dirigeant</span>
    <span class="nav-item"><svg class="nav-icon" viewBox="0 0 14 14"><rect x="2" y="7" width="3" height="6" fill="#fff"/><rect x="6" y="4" width="3" height="9" fill="#fff"/><rect x="10" y="1" width="3" height="12" fill="#fff"/></svg>Mes finances</span>
    <span class="nav-item"><svg class="nav-icon" viewBox="0 0 14 14"><rect x="3" y="1" width="8" height="12" fill="#fff"/></svg>Statut</span>
    <span class="nav-item"><svg class="nav-icon" viewBox="0 0 14 14"><path d="M3 1h3l1 4-2 1c1 2 2 3 4 4l1-2 4 1v3c-6 0-11-5-11-11z" fill="#fff"/></svg>Contact</span>
  </nav>
  <div class="hero" style="height:478px">
    <div class="hero-photo" role="img" aria-label="Photo of hands with documents and a tablet on a wooden table" style="background:linear-gradient(160deg,#8a6a4d 0%,#c4a585 30%,#e8e3dc 50%,#b89574 75%,#6f5038 100%)"></div>
    <div class="hero-copy" style="top:170px">
      <div class="hero-title title-orange">CREATOR OF TRUST 100% DIGITAL - 100% HUMAN</div>
      <div class="hero-sub sub-dark">ORME CONSEIL is the result of a STRONG TECHNICAL AND MANAGERIAL EXPERIENCE</div>
      <span class="btn-start">GET STARTED</span>
    </div>
  </div>
</section>

<!-- Concept 4 -->
<section class="concept concept--four">
  <div class="topbar topbar--orange">
    <span class="contact-item">✉ contact@orme-conseil.com</span>
    <span class="contact-item">☏ 05 46 12 34 56</span>
    <span class="socials"><span></span><span></span><span></span><span></span></span>
  </div>
  <header class="header" style="height:110px;padding-right:20px">
    <div class="brand"><span class="brand-mark"></span><div><div class="brand-name">ORME CONSEIL</div><div class="brand-tagline">Créateur de Confiance</div></div></div>
    <nav class="nav" style="background:none;color:var(--grey);font-size:11px;height:110px">
      <span class="nav-item" style="padding:0 10px;color:var(--orange)"><svg class="nav-icon" viewBox="0 0 14 14"><path d="M1 7 7 1l6 6h-2v6H3V7z" fill="#f39200"/></svg>Home</span>
      <span class="nav-item" style="padding:0 10px"><svg class="nav-icon" viewBox="0 0 14 14"><rect x="2" y="4" width="10" height="8" fill="#8a8a8a"/></svg>Gérer mon entreprise</span>
      <span class="nav-item" style="padding:0 10px"><svg class="nav-icon" viewBox="0 0 14 14"><circle cx="7" cy="7" r="5" fill="#8a8a8a"/></svg>Avis d'Experts</span>
      <span class="nav-item" style="padding:0 10px"><svg class="nav-icon" viewBox="0 0 14 14"><circle cx="7" cy="5" r="3" fill="#8a8a8a"/><rect x="3" y="9" width="8" height="4" fill="#8a8a8a"/></svg>Gérer mon personnel</span>
      <span class="nav-item" style="padding:0 10px"><svg class="nav-icon" viewBox="0 0 14 14"><circle cx="7" cy="5" r="3" fill="#8a8a8a"/><rect x="3" y="9" width="8" height="4" fill="#8a8a8a"/></svg>Mon statut dirigeant</span>
      <span class="nav-item" style="padding:0 10px"><svg class="nav-icon" viewBox="0 0 14 14"><rect x="2" y="7" width="3" height="6" fill="#8a8a8a"/><rect x="6" y="4" width="3" height="9" fill="#8a8a8a"/><rect x="10" y="1" width="3" height="12" fill="#8a8a8a"/></svg>Mes finances</span>
      <span class="nav-item" style="padding:0 10px"><svg class="nav-icon" viewBox="0 0 14 14"><rect x="3" y="1" width="8" height="12" fill="#8a8a8a"/></svg>Statut</span>
      <span class="nav-item" style="padding:0 10px"><svg class="nav-icon" viewBox="0 0 14 14"><path d="M3 1h3l1 4-2 1c1 2 2 3 4 4l1-2 4 1v3c-6 0-11-5-11-11z" fill="#8a8a8a"/></svg>Contact</span>
    </nav>
  </header>
  <div class="hero" style="height:504px;border-top:3px solid var(--orange)">
    <div class="hero-photo" role="img" aria-label="Photo of two colleagues reviewing charts in a bright office" style="background:linear-gradient(100deg,#d9d6d2 0%,#f3f1ee 30%,#e4ddd4 55%,#f6f5f3 75%,#c9c3bb 100%)"></div>
    <div class="hero-copy" style="top:150px">
      <div class="hero-title title-orange">CREATOR OF TRUST 100% DIGITAL - 100% HUMAN</div>
      <div class="hero-sub sub-dark">ORME CONSEIL is the result of a STRONG TECHNICAL AND MANAGERIAL EXPERIENCE</div>
      <span class="btn-start">GET STARTED</span>
    </div>
  </div>
</section>

</body>
</html>
```